We are a hi end limo company . We use Valdan Kovo strider van's custom made for first class travel . Each van has captains chairs Flat screen TV , usb ports , bar . We specialize in Wine tours and weddings , but can handle any of your transportation needs example s; night out in town , Plays, Concerts . Very comfortable like sitting in your living room , we are safe and reliable and professional

Target Market(s)

wine tasting , Travel to Cedar Bay Wine country , Transportation ,Weddings

Industry/Entity Type

Tv

Contact Information for Business Card

Birch Hollow Luxury Carriers 555 248 9017, Daniel R Trosk Daniel@Birchhollowluxurycarriers.example www.Birchhollowluxurycarriers.example Pellbrook NY, reservations only

Requirements
Must have
• Reservations only
Nice to have
• Something Bold eye catching colors Black gloss
• Reliable safe
• Valdan kovo strider logo

```html
<!DOCTYPE html>
<html lang="en">
<head>
<meta charset="utf-8">
<title>Birch Hollow Luxury Carriers — Business Card</title>
<link rel="stylesheet" href="https://fonts.googleapis.com/css2?family=Oswald:wght@700&family=Open+Sans:wght@400;600;700&family=Kaushan+Script&display=swap">
<style>
  :root {
    --canvas-bg: #e6e4e1;
    --card-white: #ffffff;
    --card-black: #231f20;
    --ink-dark: #1d1b1c;
    --ink-light: #ffffff;
    --shadow: rgba(0, 0, 0, 0.18);
  }
  * { margin: 0; padding: 0; box-sizing: border-box; }
  html, body {
    width: 1200px;
    height: 900px;
    overflow: hidden;
    background: var(--canvas-bg);
  }
  .canvas {
    width: 1200px;
    height: 900px;
    display: flex;
    align-items: center;
    justify-content: center;
    gap: 50px;
  }
  .card {
    position: relative;
    width: 525px;
    height: 300px;
    box-shadow: 0 6px 18px var(--shadow);
  }
  .card--front { background: var(--card-white); color: var(--ink-dark); }
  .card--back {
    background: var(--card-black);
    color: var(--ink-light);
    display: flex;
    flex-direction: column;
    align-items: center;
    justify-content: center;
  }
  .brand { text-align: center; }
  .card--front .brand {
    position: absolute;
    top: 28px;
    left: 0;
    right: 0;
  }
  .brand__name {
    font-family: "Oswald", "Arial Narrow", sans-serif;
    font-weight: 700;
    font-size: 38px;
    letter-spacing: 1.5px;
    line-height: 1;
  }
  .card--back .brand__name { font-size: 46px; letter-spacing: 2px; }
  .brand__tagline {
    font-family: "Kaushan Script", cursive;
    font-size: 17px;
    line-height: 1;
    margin-top: 6px;
    margin-left: 70px;
  }
  .card--back .brand__tagline { font-size: 21px; margin-left: 90px; margin-top: 8px; }
  .contact {
    position: absolute;
    top: 158px;
    left: 0;
    right: 0;
    text-align: center;
    font-family: "Open Sans", Arial, sans-serif;
  }
  .contact__name {
    font-weight: 600;
    font-size: 20px;
    margin-bottom: 4px;
  }
  .contact__line {
    font-size: 10.5px;
    line-height: 1.4;
  }
  .mark {
    position: absolute;
    left: 18px;
    bottom: 16px;
    display: flex;
    align-items: center;
    gap: 5px;
    font-family: "Open Sans", Arial, sans-serif;
    font-weight: 600;
    font-size: 9px;
  }
  .mark__dot {
    width: 14px;
    height: 14px;
    border-radius: 50%;
    background: var(--ink-dark);
  }
  .reservations {
    position: absolute;
    right: 20px;
    bottom: 18px;
    font-family: "Open Sans", Arial, sans-serif;
    font-weight: 700;
    font-size: 9px;
    letter-spacing: 0.3px;
  }
</style>
</head>
<body>
  <main class="canvas">
    <section class="card card--front" aria-label="Business card front">
      <div class="brand">
        <div class="brand__name">BIRCH HOLLOW</div>
        <div class="brand__tagline">Luxury Carriers</div>
      </div>
      <div class="contact">
        <div class="contact__name">Daniel R Trosk</div>
        <div class="contact__line">Daniel@Birchhollowluxurycarriers.example</div>
        <div class="contact__line">www.Birchhollowluxurycarriers.example</div>
        <div class="contact__line">Pellbrook NY</div>
      </div>
      <div class="mark">
        <span class="mark__dot"></span>
        <span class="mark__text">Birch Hollow</span>
      </div>
      <div class="reservations">RESERVATIONS ONLY</div>
    </section>

    <section class="card card--back" aria-label="Business card back">
      <div class="brand">
        <div class="brand__name">BIRCH HOLLOW</div>
        <div class="brand__tagline">Luxury Carriers</div>
      </div>
    </section>
  </main>
</body>
</html>
```